Small environmental consultancy needs a simple but professional web design

We are a boutique environmental consultancyand contracting business located in Margaret River in the South West of Western Australia.

We have two arms
1) Consulting which offers environmental planning, management and assessment services primarily to local government and the development industry.
2) Contracting which implements on site plans and on ground works primarily involving revegetation, bush regeneration and environmental weed control.

We need a simple yet professional web design within the wordpress platform that commmunicates professionalism, experience and technical expertise without appearing too corporate.

Something like this structure appeals:
http://verdantia.net.au/environment-services/
or
http://www.ridgefallenvironmental.com.au/index.php

(without the image gallery function)

Target Market(s)

Local Government Officers deciding on tenders;
Developers, Engineers, Town Planning consultants looking for environmental expertise

Industry/Entity Type

Business

Number of Pages Required

5+ page

Font styles to use
Sans Serif

Colors
33a6d7
9bcb3c

Requirements
Must have
• Pages required include:
• Home
• Environmental Planning and Management
• Revegetation and Regeneration Implementation (This page can mirror the Environmental Planning and Management page exactly in structure but with different text and images)
• About Us (I think that this page can be relatively simple and generic)
• Contact (I think that this page can be very simple and generic)
Nice to have
• An ability to start out basic and quicikly establish a website presence and then build in additional drop downs and pages over time.
Should not have
• It does not need a photo gallery page;
• It does not need a major amount of space dedicated to social media and blogs etc as this is not currently particularly active area for us

```html
<!DOCTYPE html>
<html lang="en">
<head>
<meta charset="utf-8">
<title>Tallowood Ecoservices</title>
<link rel="stylesheet" href="https://fonts.googleapis.com/css2?family=Open+Sans:wght@400;600;700;800&display=swap">
<style>
:root{
  --green:#8dc63f;
  --green-dark:#6fa62a;
  --blue:#33a6d7;
  --text:#555;
  --heading:#3a3a3a;
  --page:#eeeeea;
  --white:#fff;
  --footer:#262626;
  --footer-line:#3a3a3a;
  --muted:#999;
}
*{margin:0;padding:0;box-sizing:border-box}
html,body{width:1200px;height:2448px;overflow:hidden}
body{font-family:"Open Sans",Arial,sans-serif;color:var(--text);background:var(--page);position:relative}
a{color:inherit;text-decoration:none}

/* header */
.site-header{height:152px;background:var(--white);position:relative}
.brand{position:absolute;left:72px;top:22px;display:flex;align-items:center;gap:12px}
.brand-dot{width:30px;height:30px;border-radius:50%;background:var(--green)}
.brand-name{font-size:27px;font-weight:700;color:var(--green);line-height:1.05;width:230px}
.header-phone{position:absolute;right:72px;top:16px;font-size:20px;font-weight:700;color:var(--heading);display:flex;align-items:center;gap:8px}
.main-nav{position:absolute;right:72px;top:88px;display:flex;gap:26px;font-size:14px;font-weight:600;color:#666;text-transform:uppercase}
.main-nav a{padding-bottom:8px}
.main-nav a.active{color:var(--green);border-bottom:3px solid var(--green)}

/* hero */
.hero{height:548px;position:relative;background:linear-gradient(120deg,#c9cfa9 0%,#95a466 35%,#5c6f3a 60%,#b2b98f 100%)}
.hero-caption{position:absolute;left:0;top:136px;width:460px;height:128px;background:rgba(255,255,255,.9);padding:22px 0 0 72px}
.hero-caption h1{font-size:28px;font-weight:700;color:var(--green);line-height:1.2}
.hero-caption p{font-size:22px;color:#666}

/* feature cards */
.features{display:flex;gap:16px;padding:0 72px;height:320px;background:var(--white)}
.feature{width:252px}
.feature-img{height:160px}
.feature h3{font-size:15px;font-weight:800;color:var(--heading);margin:20px 0 8px;text-transform:uppercase}
.feature p{font-size:13px;line-height:1.5;color:#777}
.btn{display:inline-block;margin-top:12px;background:#cfe3ee;color:var(--blue);font-size:12px;padding:4px 12px;border-radius:3px}

/* welcome */
.welcome{height:500px;position:relative;background:var(--white);border-top:1px solid #e6e6e6}
.welcome-text{position:absolute;left:72px;top:44px;width:488px}
.welcome-title{display:flex;align-items:center;gap:14px;margin-bottom:20px}
.welcome-dot{width:56px;height:56px;border-radius:50%;background:var(--green)}
.welcome-title small{display:block;font-size:22px;color:#666}
.welcome-title strong{display:block;font-size:34px;font-weight:800;color:var(--green);line-height:1}
.welcome-text p{font-size:13px;line-height:1.6;color:#777;margin-bottom:16px}
.welcome-img{position:absolute;left:600px;top:12px;width:528px;height:468px;background:radial-gradient(circle at 55% 55%,#5fa839 0%,#8dbb58 30%,#d7d0c2 65%,#efebe4 100%)}

/* why us */
.why{height:360px;padding-top:28px}
.section-title{text-align:center;font-size:26px;font-weight:800;color:var(--heading)}
.why-grid{display:flex;gap:24px;padding:0 72px;margin-top:40px}
.why-card{width:246px;height:250px;background:var(--white);border:1px solid #ddd;text-align:center;position:relative;padding-top:96px}
.why-icon{position:absolute;left:73px;top:-30px;width:100px;height:100px;border-radius:50%;background:var(--green);display:flex;align-items:center;justify-content:center}
.why-card h4{font-size:17px;font-weight:800;color:var(--heading);line-height:1.25;text-transform:uppercase}
.why-card p{font-size:13px;color:#888;line-height:1.5;margin-top:14px;padding:0 22px}

/* testimonials */
.testimonials{height:252px;padding-top:0;text-align:center;position:relative}
.testimonials .section-title{padding-top:8px}
.testimonials blockquote{width:960px;margin:20px auto 0;font-size:13px;line-height:1.6;color:#777}
.testimonials cite{display:block;font-style:normal;font-weight:700;color:var(--blue);font-size:14px;margin-top:16px}
.stars{margin-top:6px;display:flex;justify-content:center;gap:4px}
.slider-arrow{position:absolute;top:110px;width:26px;height:26px;border-radius:50%;background:#ddd}
.slider-arrow.prev{left:40px}.slider-arrow.next{right:40px}

/* footer */
.site-footer{position:absolute;left:0;top:2160px;width:1200px;height:288px;background:var(--footer);color:#ccc;text-align:center}
.footer-contact{display:flex;justify-content:center;align-items:center;gap:60px;padding-top:28px;font-size:16px;font-weight:600}
.footer-dot{width:64px;height:64px;border-radius:50%;background:var(--green)}
.footer-nav{margin-top:26px;padding:18px 0;border-top:1px solid var(--footer-line);border-bottom:1px solid var(--footer-line);display:flex;justify-content:center;gap:36px;font-size:14px;font-weight:700;color:#ddd;text-transform:uppercase}
.copyright{margin-top:24px;font-size:12px;color:var(--muted)}
</style>
</head>
<body>

<header class="site-header">
  <a class="brand" href="#"><span class="brand-dot"></span><span class="brand-name">Tallowood Ecoservices</span></a>
  <div class="header-phone">
    <svg width="20" height="20" viewBox="0 0 24 24"><path fill="#3a3a3a" d="M6.6 10.8a15.1 15.1 0 0 0 6.6 6.6l2.2-2.2a1 1 0 0 1 1-.25 11.4 11.4 0 0 0 3.6.6 1 1 0 0 1 1 1V20a1 1 0 0 1-1 1A17 17 0 0 1 3 4a1 1 0 0 1 1-1h3.5a1 1 0 0 1 1 1c0 1.25.2 2.45.6 3.6a1 1 0 0 1-.25 1z"/></svg>
    (808) 555 01 2468
  </div>
  <nav class="main-nav">
    <a class="active" href="#">Home</a>
    <a href="#">Environmental Planning &amp; Management</a>
    <a href="#">Revegetation &amp; Regeneration Implementation</a>
    <a href="#">About Us</a>
    <a href="#">Contact</a>
  </nav>
</header>

<section class="hero" role="img" aria-label="Photo of pink blossom on a branch against a soft green background">
  <div class="hero-caption">
    <h1>Tallowood Ecoservices</h1>
    <p>Environmental Consultants</p>
  </div>
</section>

<section class="features">
  <article class="feature">
    <div class="feature-img" role="img" aria-label="Photo of red native flowers" style="background:linear-gradient(135deg,#c2361f,#6e8a3a)"></div>
    <h3>Why Tallowood?</h3>
    <p>We bring local knowledge and careful field practice to every project we take on.</p>
    <a class="btn" href="#">Read More</a>
  </article>
  <article class="feature">
    <div class="feature-img" role="img" aria-label="Photo of a fern frond" style="background:linear-gradient(135deg,#2e4a18,#7fb34a)"></div>
    <h3>Our Services</h3>
    <p>Planning, assessment and on ground works for councils and developers alike.</p>
    <a class="btn" href="#">Read More</a>
  </article>
  <article class="feature">
    <div class="feature-img" role="img" aria-label="Photo of sunlight through a forest" style="background:linear-gradient(135deg,#f1ecc4,#4f7a34)"></div>
    <h3>Current Project</h3>
    <p>Restoring a coastal reserve with native plantings and steady weed control.</p>
    <a class="btn" href="#">Read More</a>
  </article>
  <article class="feature">
    <div class="feature-img" role="img" aria-label="Photo of a wide green landscape under blue sky" style="background:linear-gradient(180deg,#8fc2e0,#6a9a3c)"></div>
    <h3>Contact Us</h3>
    <p>Talk with our team about your site, your timeline and your next steps.</p>
    <a class="btn" href="#">Read More</a>
  </article>
</section>

<section class="welcome">
  <div class="welcome-text">
    <div class="welcome-title">
      <span class="welcome-dot"></span>
      <div><small>Welcome to</small><strong>TALLOWOOD ECOSERVICES</strong></div>
    </div>
    <p>We are a boutique environmental consultancy and contracting business based in the South West. Our team works with local government and the development industry to plan, assess and manage land with care. We aim to give clear, practical advice that stands up to scrutiny and suits the site.</p>
    <p>Our contracting arm puts plans into action on the ground. We carry out revegetation, bush regeneration and weed control, working season by season to see each landscape recover and thrive over time.</p>
    <p>Whether you are preparing a tender, a development proposal or a long term management plan, we offer steady support from first survey to final report, backed by years of hands on regional experience.</p>
    <a class="btn" href="#">Read More</a>
  </div>
  <div class="welcome-img" role="img" aria-label="Photo of cupped hands holding a small green globe"></div>
</section>

<section class="why">
  <h2 class="section-title">WHY US?</h2>
  <div class="why-grid">
    <div class="why-card">
      <div class="why-icon"><svg width="50" height="50" viewBox="0 0 50 50"><path d="M10 40C10 18 26 8 42 8c0 18-10 32-30 32z" fill="#fff"/><path d="M10 40L32 18" stroke="#8dc63f" stroke-width="3"/></svg></div>
      <h4>Lorem ipsum<br>dolor sit amet</h4>
      <p>Careful planning that suits the land and the people who use it.</p>
    </div>
    <div class="why-card">
      <div class="why-icon"><svg width="52" height="52" viewBox="0 0 52 52" fill="none" stroke="#fff" stroke-width="3"><circle cx="26" cy="26" r="22"/><ellipse cx="26" cy="26" rx="10" ry="22"/><path d="M4 26h44M8 15h36M8 37h36"/></svg></div>
      <h4>Lorem ipsum<br>dolor sit amet</h4>
      <p>Broad experience across coastal, forest and farming landscapes.</p>
    </div>
    <div class="why-card">
      <div class="why-icon"><svg width="46" height="50" viewBox="0 0 46 50"><rect x="6" y="4" width="34" height="42" rx="3" fill="#fff"/><path d="M13 16h20M13 24h20M13 32h14" stroke="#8dc63f" stroke-width="3"/></svg></div>
      <h4>Lorem ipsum<br>dolor sit amet</h4>
      <p>Clear reports that councils and planners can rely upon.</p>
    </div>
    <div class="why-card">
      <div class="why-icon"><svg width="56" height="46" viewBox="0 0 56 46" fill="#fff"><circle cx="18" cy="12" r="8"/><circle cx="38" cy="12" r="8"/><path d="M4 42c0-12 6-18 14-18s14 6 14 18zM24 42c0-12 6-18 14-18s14 6 14 18z"/></svg></div>
      <h4>Lorem ipsum<br>dolor sit amet</h4>
      <p>A small local team that stays with you from start to finish.</p>
    </div>
  </div>
</section>

<section class="testimonials">
  <h2 class="section-title">CLIENT'S TESTIMONIALS</h2>
  <span class="slider-arrow prev"></span><span class="slider-arrow next"></span>
  <blockquote>The team handled our reserve management plan with great care and skill. Their field work was thorough, their reports were clear, and they met every deadline we set. The revegetation works have transformed the site, and our community has noticed the change. We would happily work with them again on future projects across the shire.</blockquote>
  <cite>- MARK DALTON</cite>
  <div class="stars">
    <svg width="96" height="18" viewBox="0 0 96 18"><g fill="#f2b01e"><path id="s" d="M9 1l2.4 5.3 5.6.6-4.2 3.8 1.2 5.6L9 13.5 4 16.3l1.2-5.6L1 6.9l5.6-.6z"/><use href="#s" x="19"/><use href="#s" x="38"/></g><g fill="#ccc"><use href="#s" x="57"/><use href="#s" x="76"/></g></svg>
  </div>
</section>

<footer class="site-footer">
  <div class="footer-contact">
    <span>(808) 555 01 2468</span>
    <span class="footer-dot"></span>
    <span>info@tallowoodeco.com</span>
  </div>
  <nav class="footer-nav">
    <a href="#">Home</a>
    <a href="#">Environmental Planning &amp; Management</a>
    <a href="#">Revegetation &amp; Regeneration Implementation</a>
    <a href="#">About Us</a>
    <a href="#">Contact</a>
  </nav>
  <p class="copyright">© 2024 Tallowood Ecoservices. All Rights Reserved</p>
</footer>

</body>
</html>
```